Harwell Properties Business Cards

I would like a business card that includes myself and my partner.
Includes: Logo, office #, email, website, our names, our numbers and possibly the address. I would also like the logo to be embossed and the card to be horizontal.
There is a photo of our yard signs to give you an idea of the colors of our business.

Target Market(s)

Everyone in real estate market.
We are in a rural area. Our clientele are from all socioeconomic backgrounds.

Industry/Entity Type

Real Estate Agent

Contact Information for Business Card

Company Name: Harwell Properties
Our Names, Titles & Cell #'s : Dana Harwell-Broker (555).613.2947, Marla Harwell-Realtor (555).730.5816
Office #: (555).264.1300
Website: harwellproperties.example
Joint Email: harwell@harwellproperties.example
Office Address: 418C W. Pell Creek St.
Brazoria, TX. 00518

Font styles to use
Serif

Requirements
Must have
• HORIZONTAL, Logo, Myself and my partners names, Our cell #'s, our office #, our website, our email address
Nice to have
• Embossed logo, office address, our titles.

```html
<!DOCTYPE html>
<html lang="en">
<head>
<meta charset="utf-8">
<title>Harwell Properties Business Card</title>
<link rel="stylesheet" href="https://fonts.googleapis.com/css2?family=EB+Garamond:wght@500;600;700&display=swap">
<style>
  :root {
    --page: #efece6;
    --card-purple: #4a2163;
    --ink-white: #ffffff;
    --shadow: rgba(40, 20, 50, 0.25);
  }
  html, body {
    margin: 0;
    width: 1200px;
    height: 1200px;
    overflow: hidden;
    background: var(--page);
  }
  .canvas {
    position: relative;
    width: 1200px;
    height: 1200px;
  }
  .business-card {
    position: absolute;
    left: 100px;
    top: 314px;
    width: 1000px;
    height: 572px;
    background: var(--card-purple);
    box-shadow: 0 10px 30px var(--shadow);
    font-family: "EB Garamond", Georgia, serif;
    color: var(--ink-white);
  }
  .card-frame {
    position: absolute;
    inset: 22px;
    border: 3px solid var(--ink-white);
  }
  .brand {
    position: absolute;
    left: 300px;
    top: 44px;
    width: 560px;
    height: 190px;
  }
  .brand-dot {
    position: absolute;
    left: 0;
    top: 20px;
    width: 96px;
    height: 96px;
    border-radius: 50%;
    background: var(--ink-white);
  }
  .brand-name {
    position: absolute;
    left: 124px;
    top: 6px;
    margin: 0;
    font-size: 86px;
    font-weight: 700;
    letter-spacing: 2px;
    line-height: 1;
    text-transform: uppercase;
  }
  .brand-rule {
    position: absolute;
    left: 124px;
    top: 108px;
    width: 420px;
    height: 0;
    border-top: 2px solid var(--ink-white);
  }
  .brand-sub {
    position: absolute;
    left: 180px;
    top: 112px;
    margin: 0;
    font-size: 58px;
    font-weight: 700;
    line-height: 1;
  }
  .agents {
    position: absolute;
    left: 60px;
    right: 60px;
    top: 244px;
    display: flex;
    justify-content: space-around;
  }
  .agent {
    width: 400px;
    text-align: center;
  }
  .agent-name {
    margin: 0;
    font-size: 40px;
    font-weight: 700;
    line-height: 1.1;
  }
  .agent-detail {
    margin: 0;
    font-size: 26px;
    font-weight: 600;
    line-height: 1.3;
  }
  .office-contact {
    position: absolute;
    left: 70px;
    top: 352px;
  }
  .office-phone {
    margin: 0;
    font-size: 44px;
    font-weight: 700;
    line-height: 1.05;
  }
  .office-address {
    margin: 0;
    font-size: 28px;
    font-weight: 600;
    line-height: 1.2;
  }
  .online-contact {
    position: absolute;
    right: 70px;
    top: 430px;
    text-align: right;
  }
  .online-contact p {
    margin: 0;
    font-size: 30px;
    font-weight: 600;
    line-height: 1.35;
  }
</style>
</head>
<body>
<main class="canvas">
  <section class="business-card" aria-label="Harwell Properties business card">
    <div class="card-frame"></div>

    <div class="brand">
      <span class="brand-dot" aria-hidden="true"></span>
      <h1 class="brand-name">Harwell</h1>
      <span class="brand-rule" aria-hidden="true"></span>
      <p class="brand-sub">Properties</p>
    </div>

    <div class="agents">
      <div class="agent">
        <p class="agent-name">Dana Harwell</p>
        <p class="agent-detail">Broker · Cell (555).613.2947</p>
      </div>
      <div class="agent">
        <p class="agent-name">Marla Harwell</p>
        <p class="agent-detail">Realtor · Cell (555).730.5816</p>
      </div>
    </div>

    <div class="office-contact">
      <p class="office-phone">555.264.1300</p>
      <p class="office-address">418C W. Pell Creek St.</p>
      <p class="office-address">Brazoria, TX. 00518</p>
    </div>

    <div class="online-contact">
      <p class="website">www.harwellproperties.example</p>
      <p class="email">harwell@harwellproperties.example</p>
    </div>
  </section>
</main>
</body>
</html>
```